The Orchard of Virtue Customized for my Business

Hi! I am interested in getting some design ideas to take this Orchard of Virtue and put a bit of branding of my business into it. Open to any and all designs, this is intended to put on a 20"x24" or 16"x20" canvas so I can have it in my office for team training purposes. I have included a picture of the wall this canvas will go on. Thank you!

```html
<!DOCTYPE html>
<html lang="en">
<head>
<meta charset="utf-8">
<title>Orchard of Virtue</title>
<link href="https://fonts.googleapis.com/css2?family=Montserrat:wght@400;600;700;800&display=swap" rel="stylesheet">
<style>
  :root {
    --canvas: #e6e6e6;
    --paper: #ffffff;
    --ink: #2a2c30;
    --ink-soft: #5b5e64;
    --brand-blue: #29a3dc;
    --pyramid: #2b2d32;
    --pyramid-edge: #8d9096;
    --block-body: #1c1e22;
    --block-text: #d8dadd;
    --white: #ffffff;
  }
  html, body {
    margin: 0;
    width: 1200px;
    height: 896px;
    overflow: hidden;
    background: var(--canvas);
    font-family: "Montserrat", sans-serif;
  }
  .poster {
    position: absolute;
    left: 240px;
    top: 18px;
    width: 720px;
    height: 860px;
    background: var(--paper);
  }
  .brand {
    position: absolute;
    left: 36px;
    top: 30px;
    display: flex;
    flex-direction: column;
    align-items: center;
    gap: 10px;
  }
  .brand-name {
    font-weight: 700;
    font-size: 24px;
    color: var(--brand-blue);
    letter-spacing: 0.5px;
  }
  .brand-dot {
    width: 56px;
    height: 56px;
    border-radius: 50%;
    background: var(--brand-blue);
  }
  .pyramid-art { position: absolute; left: 0; top: 0; }
  .block-title { font-weight: 700; font-size: 9px; fill: var(--white); }
  .block-text { font-weight: 400; font-size: 7px; fill: var(--block-text); }
  .side-title { font-weight: 700; font-size: 11px; fill: var(--ink); }
  .side-text { font-weight: 400; font-size: 8px; fill: var(--ink-soft); }
  .banner-title { font-weight: 800; font-size: 28px; fill: var(--white); letter-spacing: 0.5px; }
  .site-link {
    position: absolute;
    left: 210px;
    top: 812px;
    width: 300px;
    height: 22px;
    border-radius: 11px;
    background: var(--brand-blue);
    color: var(--white);
    font-size: 10px;
    font-weight: 600;
    line-height: 22px;
    text-align: center;
  }
</style>
</head>
<body>
<main class="poster">
  <div class="brand">
    <span class="brand-name">Kestrelford</span>
    <span class="brand-dot"></span>
  </div>

  <svg class="pyramid-art" width="720" height="860" viewBox="0 0 720 860" aria-labelledby="pyramid-heading">
    <title id="pyramid-heading">The Orchard of Virtue</title>

    <polygon points="362,150 70,560 655,560" fill="var(--pyramid)" stroke="var(--pyramid-edge)" stroke-width="4"/>
    <circle cx="362" cy="215" r="12" fill="var(--brand-blue)"/>

    <!-- tier 1 -->
    <g class="block"><rect x="307" y="255" width="110" height="45" rx="6" fill="var(--block-body)"/><rect x="307" y="255" width="110" height="16" rx="6" fill="var(--brand-blue)"/><text class="block-title" x="362" y="266" text-anchor="middle">Client Delight</text><text class="block-text" x="362" y="286" text-anchor="middle">Exceed every promise</text></g>

    <!-- tier 2 -->
    <g class="block"><rect x="259" y="310" width="100" height="45" rx="6" fill="var(--block-body)"/><rect x="259" y="310" width="100" height="16" rx="6" fill="var(--brand-blue)"/><text class="block-title" x="309" y="321" text-anchor="middle">Quality Work</text><text class="block-text" x="309" y="341" text-anchor="middle">Check it twice</text></g>
    <g class="block"><rect x="365" y="310" width="100" height="45" rx="6" fill="var(--block-body)"/><rect x="365" y="310" width="100" height="16" rx="6" fill="var(--brand-blue)"/><text class="block-title" x="415" y="321" text-anchor="middle">Fair Pricing</text><text class="block-text" x="415" y="341" text-anchor="middle">Honest value always</text></g>

    <!-- tier 3 -->
    <g class="block"><rect x="218" y="365" width="92" height="45" rx="6" fill="var(--block-body)"/><rect x="218" y="365" width="92" height="16" rx="6" fill="var(--brand-blue)"/><text class="block-title" x="264" y="376" text-anchor="middle">Clear Notes</text><text class="block-text" x="264" y="396" text-anchor="middle">Write it down</text></g>
    <g class="block"><rect x="316" y="365" width="92" height="45" rx="6" fill="var(--block-body)"/><rect x="316" y="365" width="92" height="16" rx="6" fill="var(--brand-blue)"/><text class="block-title" x="362" y="376" text-anchor="middle">Open Door</text><text class="block-text" x="362" y="396" text-anchor="middle">Ask anytime</text></g>
    <g class="block"><rect x="414" y="365" width="92" height="45" rx="6" fill="var(--block-body)"/><rect x="414" y="365" width="92" height="16" rx="6" fill="var(--brand-blue)"/><text class="block-title" x="460" y="376" text-anchor="middle">Quick Reply</text><text class="block-text" x="460" y="396" text-anchor="middle">Answer same day</text></g>

    <!-- tier 4 -->
    <g class="block"><rect x="181" y="420" width="86" height="45" rx="6" fill="var(--block-body)"/><rect x="181" y="420" width="86" height="16" rx="6" fill="var(--brand-blue)"/><text class="block-title" x="224" y="431" text-anchor="middle">Safety First</text><text class="block-text" x="224" y="451" text-anchor="middle">Protect the team</text></g>
    <g class="block"><rect x="273" y="420" width="86" height="45" rx="6" fill="var(--block-body)"/><rect x="273" y="420" width="86" height="16" rx="6" fill="var(--brand-blue)"/><text class="block-title" x="316" y="431" text-anchor="middle">Neat Desk</text><text class="block-text" x="316" y="451" text-anchor="middle">Order saves time</text></g>
    <g class="block"><rect x="365" y="420" width="86" height="45" rx="6" fill="var(--block-body)"/><rect x="365" y="420" width="86" height="16" rx="6" fill="var(--brand-blue)"/><text class="block-title" x="408" y="431" text-anchor="middle">Shared Wins</text><text class="block-text" x="408" y="451" text-anchor="middle">Celebrate together</text></g>
    <g class="block"><rect x="457" y="420" width="86" height="45" rx="6" fill="var(--block-body)"/><rect x="457" y="420" width="86" height="16" rx="6" fill="var(--brand-blue)"/><text class="block-title" x="500" y="431" text-anchor="middle">Fresh Ideas</text><text class="block-text" x="500" y="451" text-anchor="middle">Try something new</text></g>

    <!-- tier 5 -->
    <g class="block"><rect x="145" y="475" width="82" height="45" rx="6" fill="var(--block-body)"/><rect x="145" y="475" width="82" height="16" rx="6" fill="var(--brand-blue)"/><text class="block-title" x="186" y="486" text-anchor="middle">Onboarding</text><text class="block-text" x="186" y="506" text-anchor="middle">Welcome new hires</text></g>
    <g class="block"><rect x="233" y="475" width="82" height="45" rx="6" fill="var(--block-body)"/><rect x="233" y="475" width="82" height="16" rx="6" fill="var(--brand-blue)"/><text class="block-title" x="274" y="486" text-anchor="middle">Documentation</text><text class="block-text" x="274" y="506" text-anchor="middle">Record each step</text></g>
    <g class="block"><rect x="321" y="475" width="82" height="45" rx="6" fill="var(--block-body)"/><rect x="321" y="475" width="82" height="16" rx="6" fill="var(--brand-blue)"/><text class="block-title" x="362" y="486" text-anchor="middle">Follow-Up</text><text class="block-text" x="362" y="506" text-anchor="middle">Close every loop</text></g>
    <g class="block"><rect x="409" y="475" width="82" height="45" rx="6" fill="var(--block-body)"/><rect x="409" y="475" width="82" height="16" rx="6" fill="var(--brand-blue)"/><text class="block-title" x="450" y="486" text-anchor="middle">Scheduling</text><text class="block-text" x="450" y="506" text-anchor="middle">Plan the week</text></g>
    <g class="block"><rect x="497" y="475" width="82" height="45" rx="6" fill="var(--block-body)"/><rect x="497" y="475" width="82" height="16" rx="6" fill="var(--brand-blue)"/><text class="block-title" x="538" y="486" text-anchor="middle">Budgeting</text><text class="block-text" x="538" y="506" text-anchor="middle">Mind each dollar</text></g>

    <!-- left side values -->
    <g class="side-value"><circle cx="300" cy="184" r="9" fill="var(--ink)"/><text class="side-title" x="312" y="204" text-anchor="end">Hospitality</text><text class="side-text" x="312" y="215" text-anchor="end">Greet warmly</text></g>
    <g class="side-value"><circle cx="242" cy="264" r="9" fill="var(--ink)"/><text class="side-title" x="255" y="284" text-anchor="end">Humor</text><text class="side-text" x="255" y="295" text-anchor="end">Laugh often</text></g>
    <g class="side-value"><circle cx="185" cy="344" r="9" fill="var(--ink)"/><text class="side-title" x="198" y="364" text-anchor="end">Thrift</text><text class="side-text" x="198" y="375" text-anchor="end">Spend wisely</text></g>
    <g class="side-value"><circle cx="128" cy="424" r="9" fill="var(--ink)"/><text class="side-title" x="141" y="444" text-anchor="end">Gratitude</text><text class="side-text" x="141" y="455" text-anchor="end">Say thanks</text></g>
    <g class="side-value"><circle cx="72" cy="504" r="9" fill="var(--ink)"/><text class="side-title" x="84" y="524" text-anchor="end">Stewardship</text><text class="side-text" x="84" y="535" text-anchor="end">Improve things</text></g>

    <!-- right side values -->
    <g class="side-value"><circle cx="424" cy="184" r="9" fill="var(--ink)"/><text class="side-title" x="412" y="204">Punctuality</text><text class="side-text" x="412" y="215">Arrive early</text></g>
    <g class="side-value"><circle cx="482" cy="264" r="9" fill="var(--ink)"/><text class="side-title" x="469" y="284">Generosity</text><text class="side-text" x="469" y="295">Give freely</text></g>
    <g class="side-value"><circle cx="539" cy="344" r="9" fill="var(--ink)"/><text class="side-title" x="526" y="364">Tidiness</text><text class="side-text" x="526" y="375">Stay organized</text></g>
    <g class="side-value"><circle cx="596" cy="424" r="9" fill="var(--ink)"/><text class="side-title" x="583" y="444">Mentoring</text><text class="side-text" x="583" y="455">Teach others</text></g>
    <g class="side-value"><circle cx="652" cy="504" r="9" fill="var(--ink)"/><text class="side-title" x="640" y="524">Balance</text><text class="side-text" x="640" y="535">Rest well</text></g>

    <!-- title banner -->
    <rect x="60" y="540" width="605" height="80" rx="18" fill="var(--pyramid)" stroke="var(--pyramid-edge)" stroke-width="3"/>
    <rect x="112" y="560" width="500" height="40" rx="20" fill="var(--brand-blue)"/>
    <circle cx="88" cy="580" r="14" fill="var(--white)"/>
    <circle cx="637" cy="580" r="14" fill="var(--white)"/>
    <text class="banner-title" x="362" y="590" text-anchor="middle">THE ORCHARD OF VIRTUE</text>
  </svg>

  <div class="site-link">www.kestrelford-advisors.com</div>
</main>
</body>
</html>
```